WordPress Site That Reviews Footwear

We need a wordpress web design for an affiliate site called TarnWisp. We review and do roundups on footwear products. The final design should be clean and mobile friendly. The site should be built with Gutenberg page builder. We like the design of https://petalharvin.com/.

Target Market(s)

USA

Industry/Entity Type

Footwear

Logo Text

TarnWisp

Number of Pages Required

4 page

Font styles to use
Serif
Sans Serif

Requirements
Must have
• Wordpress site
Blog post
Page
Categories
Homepage

```html
<!DOCTYPE html>
<html lang="en">
<head>
<meta charset="utf-8">
<title>TarnWisp — Page Designs</title>
<link rel="stylesheet" href="https://fonts.googleapis.com/css2?family=Playfair+Display:wght@400;700;900&family=Poppins:wght@400;500;600&display=swap">
<style>
:root{
  --board:#2a292f;
  --band:#3c3b41;
  --paper:#ffffff;
  --mist:#f4f4f4;
  --line:#e4e4e4;
  --ink:#1e1e21;
  --muted:#77777c;
  --red:#e8392f;
  --slate:#557b88;
  --serif:'Playfair Display', Georgia, serif;
  --sans:'Poppins', Arial, sans-serif;
}
*{box-sizing:border-box;margin:0;padding:0}
html,body{width:680px;height:1200px;overflow:hidden;background:var(--board)}
ul{list-style:none}
.board{position:relative;width:680px;height:1200px;overflow:hidden;background:var(--board);font-family:var(--sans);color:var(--ink)}
.board-wave{position:absolute;inset:0}
.board-title{position:absolute;top:44px;left:0;width:680px;text-align:center;font-family:var(--serif);font-weight:700;font-size:72px;line-height:1;color:var(--paper);letter-spacing:1px}
.page-label{position:absolute;font-family:var(--serif);font-weight:900;font-size:14.5px;color:var(--paper);letter-spacing:.3px}

/* page frames */
.page{position:absolute;width:197px;background:var(--paper);overflow:hidden;box-shadow:0 6px 18px rgba(0,0,0,.4)}
.page *{position:absolute}
.page ul li,.page p span,.page b,.page i,.page .flow *{position:static}
.home{left:110px;top:183px;height:522px}
.about{left:349px;top:242px;height:347px}
.detail{left:343px;top:648px;height:448px}
.archive{left:110px;top:760px;height:369px}

/* nav */
.site-nav{left:0;top:0;width:197px;height:15px;background:var(--paper);font-size:1.8px;font-weight:600;letter-spacing:.1px;color:var(--ink)}
.nav-links{left:14px;top:6.6px;white-space:nowrap}
.nav-links span,.nav-utility span{position:static;margin-right:2.6px}
.nav-logo{left:0;width:197px;top:4.8px;text-align:center;font-family:var(--serif);font-weight:700;font-size:5px}
.nav-utility{left:134px;top:6.6px;white-space:nowrap}
.nav-icons{left:167px;top:5.5px}

/* shared type */
.section-title{left:0;width:197px;text-align:center;font-family:var(--serif);font-size:5px;font-weight:400}
.section-title b{font-weight:700}
.section-sub{left:0;width:197px;text-align:center;font-size:2px;color:var(--muted)}
.photo{border-radius:1px}
.red-rule{height:.5px;width:6px;background:var(--red)}

/* footer */
.site-footer{left:0;bottom:0;width:197px;height:65px;background:var(--mist)}
.foot-col h4{position:static;font-family:var(--serif);font-weight:700;font-size:2.7px;margin-bottom:2.2px}
.foot-col li{font-size:1.8px;line-height:4.4px;color:#4a4a4f}
.foot-col{top:12.5px}
.c1{left:21px}.c2{left:60px}.c3{left:97px;width:36px}.c4{left:140px}
.contact-item{position:static !important;display:block;padding-left:4px;font-size:1.8px;line-height:2.4px;color:#4a4a4f;margin-bottom:1.6px}
.dot-row{position:static !important;display:flex;gap:1px;margin-bottom:3px}
.dot-row span{position:static;width:3.8px;height:3.8px;border-radius:50%}
.pay-row{position:static !important;display:flex;gap:1.6px}
.pay-row span{position:static;width:6px;height:3.6px;border-radius:.6px}
.copyright{left:0;width:197px;bottom:5px;text-align:center;font-size:1.7px;font-weight:600;color:#4a4a4f}
.copy-rule{left:21px;right:21px;bottom:9.5px;height:.3px;background:var(--line)}
.to-top{right:8px;bottom:6px;width:6px;height:6px;border-radius:50%;background:var(--red)}

/* home */
.hero-panel{left:97px;top:21px;width:100px;height:87px;background:var(--mist)}
.hero-title{left:14px;top:33px;font-family:var(--serif);font-size:8.6px;line-height:9.4px}
.hero-title b{font-weight:700}
.hero-copy{left:14px;top:63px;width:72px;font-size:2.1px;line-height:2.9px;color:var(--muted)}
.hero-link{left:14px;top:74px;font-size:1.9px;font-weight:600;border-bottom:.3px solid var(--ink)}
.cat-grid{left:112px;top:30px;width:70px;display:grid;grid-template-columns:repeat(3,22px);gap:2px}
.cat-tile{position:static !important;height:20.5px;background:var(--paper);box-shadow:0 .5px 2px rgba(0,0,0,.12);display:flex;flex-direction:column;align-items:center;justify-content:center;gap:3px}
.cat-tile i{width:10px;height:4px;border:.4px solid var(--ink);border-radius:2px 3px 1px 1px}
.cat-tile span{font-size:1.7px;font-weight:500}
.promo{left:0;top:151px;width:147px;height:95px;background:var(--slate);color:var(--paper)}
.promo-name{left:14px;top:18px;font-family:var(--serif);font-size:5px}
.promo-tag{left:14px;top:24.5px;font-family:var(--serif);font-size:1.7px}
.promo-price{left:14px;top:30px;font-family:var(--serif);font-size:10.5px}
.promo-copy{left:14px;top:46px;width:74px;font-size:1.8px;line-height:2.7px}
.swatches{left:14px;top:61px;display:flex;gap:1px}
.swatches span{position:static;width:3.6px;height:3.6px;border-radius:50%}
.promo-btn{left:14px;top:70px;width:32px;height:7px;background:var(--paper);color:var(--ink);font-size:1.8px;font-weight:600;text-align:center;line-height:7px}
.promo-circle{left:113px;top:162px;width:72px;height:72px;border-radius:50%;background:var(--paper);box-shadow:0 1px 4px rgba(0,0,0,.15)}
.callout{font-size:1.8px;font-weight:600;text-align:center;line-height:2.3px}
.post-card{top:385px;width:41px;height:55px;background:var(--paper);box-shadow:0 .6px 2.5px rgba(0,0,0,.14)}
.post-card .photo{left:0;top:0;width:41px;height:29px}
.card-meta{left:3px;top:33px;font-size:1.4px;color:var(--muted)}
.card-title{left:3px;top:36.5px;width:30px;font-family:var(--serif);font-weight:700;font-size:2.6px;line-height:3px}
.card-copy{left:3px;top:43.5px;width:34px;font-size:1.5px;line-height:2.1px;color:var(--muted)}

/* about */
.inner-hero{left:0;top:15px;width:197px;height:54px}
.inner-hero h1{left:14px;top:18px;font-family:var(--serif);font-weight:700;font-size:9px;color:var(--paper)}
.inner-hero p{left:14px;top:30px;width:56px;font-size:1.9px;line-height:2.6px;color:var(--paper)}
.block-title{left:27px;font-family:var(--serif);font-size:8px;line-height:8.5px}
.block-title b{font-weight:700}
.copy-col{left:79px;width:92px;font-size:1.9px;line-height:2.8px;color:#55555a}
.flow p{margin-bottom:2.6px}
.side-title{left:27px;width:44px;font-family:var(--serif);font-size:4.1px;line-height:4.6px}
.side-title b{font-weight:700}
.team-photo{top:213px;width:28px;height:28px}
.team-name{top:246px;font-family:var(--serif);font-weight:700;font-size:2.7px}
.team-role{top:250px;font-size:1.6px;color:var(--muted)}
.team-copy{top:253px;width:24px;font-size:1.6px;line-height:2.3px;color:#55555a}

/* blog */
.topics-title{left:140px;font-family:var(--serif);font-size:5px}
.topics-title b{font-weight:700}
.topic-list{left:140px;width:44px}
.topic-list li{font-size:1.75px;height:8.75px;line-height:8.4px;border-bottom:.3px solid var(--line);display:flex;justify-content:space-between;color:#3a3a3e}
.post-row{left:14px;width:115px;height:30px}
.post-row .photo{left:0;top:0;width:46px;height:30px}
.row-meta{left:51px;top:2px;font-size:1.5px;color:var(--muted)}
.row-title{left:51px;top:5.5px;font-family:var(--serif);font-weight:700;font-size:3.6px}
.row-copy{left:51px;top:11px;width:62px;font-size:1.75px;line-height:2.5px;color:var(--muted)}
.row-read{left:51px;top:21.5px;font-size:1.5px;font-weight:600}
.pager{left:14px;top:282px;display:flex;gap:3.6px;align-items:center}
.pager span{position:static;width:6.4px;height:6.4px;border-radius:50%;font-size:2.2px;line-height:6.4px;text-align:center}
.detail-copy{left:15px;width:111px;font-size:1.75px;line-height:2.55px;color:#55555a}
.detail-copy h3{font-size:2.5px;font-weight:600;color:var(--ink);margin:3.5px 0 1.2px}
.share-btns{left:15px;top:131px;display:flex;gap:1.2px}
.share-btns span{position:static;width:17px;height:4px;font-size:1.3px;font-weight:600;color:var(--paper);line-height:4px;text-align:center}
.share-bar{left:15px;top:235px;width:111px;height:10px;background:#2b2d37;color:var(--paper);font-family:var(--serif);font-size:1.9px;font-weight:700;line-height:10px;padding-left:7px}
.reply-box{left:15px;top:287px;width:111px;height:77px;background:var(--mist)}
.field{height:6.5px;background:var(--paper);font-size:1.5px;line-height:6.5px;padding-left:3px;color:var(--muted)}
</style>
</head>
<body>
<main class="board">
  <svg class="board-wave" width="680" height="1200" viewBox="0 0 680 1200" aria-hidden="true">
    <path d="M0 487 C120 395 230 382 330 376 S560 322 680 331 L680 822 C560 832 420 852 300 872 S80 922 0 946 Z" fill="var(--band)"/>
  </svg>

  <h1 class="board-title">TarnWisp</h1>

  <h2 class="page-label" style="left:110px;top:160px">HOME</h2>
  <h2 class="page-label" style="left:349px;top:220px">ABOUT US</h2>
  <h2 class="page-label" style="left:343px;top:626px">BLOG DETAIL</h2>
  <h2 class="page-label" style="left:110px;top:738px">BLOG PAGE</h2>

  <!-- HOME -->
  <section class="page home">
    <div class="hero-panel"></div>
    <header class="site-nav" style="background:transparent">
      <div class="nav-links"><span>MEN ▾</span><span>WOMEN ▾</span><span>KIDS ▾</span><span>FAVORITES</span><span>CUSTOMIZE</span></div>
      <div class="nav-logo">TarnWisp</div>
      <div class="nav-utility"><span>ABOUT</span><span>CONTACT US</span></div>
      <svg class="nav-icons" width="14" height="4" viewBox="0 0 14 4" aria-hidden="true"><circle cx="1.5" cy="1.3" r=".8" fill="none" stroke="#1e1e21" stroke-width=".35"/><path d="M.3 3.6 Q1.5 2.2 2.7 3.6" fill="none" stroke="#1e1e21" stroke-width=".35"/><circle cx="6.5" cy="1.8" r="1.1" fill="none" stroke="#1e1e21" stroke-width=".35"/><path d="M7.3 2.6 L8.2 3.5" stroke="#1e1e21" stroke-width=".35"/><path d="M10.6 1 H11.3 L12 3 H13.4 L13.8 1.6 H11.5" fill="none" stroke="#1e1e21" stroke-width=".35"/><circle cx="13.7" cy=".8" r=".7" fill="#e8392f"/></svg>
    </header>
    <h2 class="hero-title">Footwear<br>For <b>Everyone</b><br>TarnWisp</h2>
    <p class="hero-copy">Aenean sollicitudin lorem quis bibendum auctor amet nibh vulputate cursus a sit amet mauris morbi.</p>
    <span class="hero-link">CHECK OUT A FEW OF OUR FAVORITES</span>
    <svg style="left:49px;top:73px" width="12" height="5" viewBox="0 0 12 5" aria-hidden="true"><path d="M1 1 Q5 4.5 10 2.5 M8.5 1.6 L10 2.5 L9 3.9" fill="none" stroke="#e8392f" stroke-width=".35"/></svg>
    <div class="cat-grid">
      <div class="cat-tile"><i></i><span>Sandals</span></div>
      <div class="cat-tile"><i></i><span>Shoes</span></div>
      <div class="cat-tile"><i></i><span>Flats</span></div>
      <div class="cat-tile"><i></i><span>Heels</span></div>
      <div class="cat-tile"><i></i><span>Ethnic</span></div>
      <div class="cat-tile"><i></i><span>Slippers</span></div>
    </div>
    <div class="photo" role="img" aria-label="Pair of tan woven leather sandals" style="left:70px;top:76px;width:62px;height:40px;border-radius:40%;background:radial-gradient(ellipse at 50% 55%,#d98a4a,#b8662e 55%,rgba(255,255,255,0) 72%)"></div>

    <h2 class="section-title" style="top:128px">What's Your <b>TarnWisp</b></h2>
    <p class="section-sub" style="top:137px">Aenean sollicitudin lorem quis bibendum auctor amet nibh vulputate cursus a sit amet mauris morbi.</p>

    <div class="promo">
      <h3 class="promo-name">Aero Drift Knit 2</h3>
      <p class="promo-tag">Incredibly Comfortable Footwear</p>
      <p class="promo-price">$100</p>
      <p class="promo-copy">Aenean sollicitudin lorem quis bibendum auctor nisi elit cursus ipsum velit. Nam nec tellus a odio tincidunt auctor a odio. Sed non mauris vitae erat consequat auctor eu in elit taciti.</p>
      <div class="swatches"><span style="background:#fff"></span><span style="background:#3fc1ee"></span><span style="background:#f2c230"></span><span style="background:#6bd26b"></span></div>
      <span class="promo-btn">CHECK OUT A FEW</span>
    </div>
    <div class="promo-circle"></div>
    <div class="photo" role="img" aria-label="Pair of yellow leather hiking boots" style="left:125px;top:178px;width:48px;height:40px;border-radius:30%;background:radial-gradient(ellipse at 50% 50%,#e8b540,#c8922a 50%,rgba(255,255,255,0) 72%)"></div>

    <h2 class="section-title" style="top:258px">Finally... TarnWisp <b>Advice</b></h2>
    <p class="section-sub" style="top:267px">Aenean sollicitudin lorem quis bibendum auctor amet nibh vulputate cursus a sit amet mauris morbi.</p>
    <svg style="left:30px;top:282px" width="140" height="62" viewBox="0 0 140 62" aria-hidden="true"><path d="M18 12 Q30 24 38 25 M112 10 Q108 22 96 24 M116 34 Q110 44 100 46 M22 36 Q30 38 36 40 M116 46 Q112 56 96 58 M52 58 Q70 62 90 56" fill="none" stroke="#cfcfcf" stroke-width=".3"/><circle cx="18" cy="12" r=".6" fill="#999"/><circle cx="112" cy="10" r=".6" fill="#999"/><circle cx="116" cy="34" r=".6" fill="#999"/><circle cx="116" cy="46" r=".6" fill="#999"/></svg>
    <div class="photo" role="img" aria-label="Red knit running shoe" style="left:58px;top:288px;width:80px;height:48px;border-radius:30%;background:radial-gradient(ellipse at 45% 50%,#d42a24,#a8151a 55%,rgba(255,255,255,0) 72%)"></div>
    <p class="callout" style="left:32px;top:282px;width:16px">Light Weight Material</p>
    <p class="callout" style="left:122px;top:283px;width:20px">Adjustable Lacing System</p>
    <p class="callout" style="left:148px;top:298px;width:18px">Natural Fitting Comfort</p>
    <p class="callout" style="left:42px;top:314px;width:18px">Strong Midsole</p>
    <p class="callout" style="left:148px;top:314px;width:18px">Integral Support Straps</p>
    <p class="callout" style="left:66px;top:327px;width:20px">Antiodor Molded Footbed</p>

    <div class="photo" role="img" aria-label="Brown and white strappy sandal" style="left:0;top:345px;width:29px;height:23px;background:linear-gradient(135deg,#8a5a3a,#e9e1da)"></div>
    <div style="left:14px;top:355px;width:169px;height:.3px;background:var(--line)"></div>

    <h2 class="section-title" style="top:368px">Learn From The <b>Experts.</b></h2>
    <p class="section-sub" style="top:376px">Aenean sollicitudin lorem quis bibendum auctor amet nibh vulputate cursus a sit amet mauris morbi.</p>
    <article class="post-card" style="left:36px">
      <div class="photo" role="img" aria-label="Tan block heel sandals on pink" style="background:linear-gradient(135deg,#f2b6bf,#e9a09b)"></div>
      <p class="card-meta">By John • January 2021</p><h3 class="card-title">Some blog heading goes here</h3><p class="card-copy">Nisi elit consequat ipsum nec sagittis sem nibh id elit...</p>
    </article>
    <article class="post-card" style="left:78.5px">
      <div class="photo" role="img" aria-label="White sneakers on grey" style="background:linear-gradient(135deg,#d4d4d4,#b9b9b9)"></div>
      <p class="card-meta">By John • January 2021</p><h3 class="card-title">Some blog heading goes here</h3><p class="card-copy">Nisi elit consequat ipsum nec sagittis sem nibh id elit...</p>
    </article>
    <article class="post-card" style="left:121px">
      <div class="photo" role="img" aria-label="Black pumps on a beige floor" style="background:linear-gradient(135deg,#f0c8a6,#d79e78)"></div>
      <p class="card-meta">By John • January 2021</p><h3 class="card-title">Some blog heading goes here</h3><p class="card-copy">Nisi elit consequat ipsum nec sagittis sem nibh id elit...</p>
    </article>

    <footer class="site-footer">
      <div class="foot-col c1"><h4>Let us help you</h4><ul><li>Search</li><li>About Us</li><li>Footwear Size</li><li>Care Guide</li><li>Shipping</li><li>Contact</li><li>FAQS</li></ul></div>
      <div class="foot-col c2"><h4>Information</h4><ul><li>Site Map</li><li>Terms &amp; Condition</li><li>Privacy Policy</li><li>FAQs</li><li>Customer Service</li><li>Disclaimer</li></ul></div>
      <div class="foot-col c3"><h4>Contact Us</h4><span class="contact-item">Email:<br>hello@tarnwisp.com</span><span class="contact-item">Phone:<br>(+00) 123 456 7890</span><span class="contact-item">Office Location:<br>Some address line goes here city name</span></div>
      <div class="foot-col c4"><h4>Stay Connected</h4><div class="dot-row"><span style="background:#3d5a98"></span><span style="background:#3fa6e0"></span><span style="background:#d2407e"></span></div><h4>Payment Method</h4><div class="pay-row"><span style="background:#dfe3ea"></span><span style="background:#2a3f9e"></span><span style="background:#2b2b2b"></span><span style="background:#eaeaea"></span></div></div>
      <div class="copy-rule"></div>
      <p class="copyright">© COPYRIGHT 2021 - ALL RIGHTS RESERVED</p>
      <span class="to-top"></span>
    </footer>
  </section>

  <!-- ABOUT -->
  <section class="page about">
    <header class="site-nav">
      <div class="nav-links"><span>MEN ▾</span><span>WOMEN ▾</span><span>KIDS ▾</span><span>FAVORITES</span><span>CUSTOMIZE</span></div>
      <div class="nav-logo">TarnWisp</div>
      <div class="nav-utility"><span>ABOUT</span><span>CONTACT US</span></div>
      <svg class="nav-icons" width="14" height="4" viewBox="0 0 14 4" aria-hidden="true"><circle cx="1.5" cy="1.3" r=".8" fill="none" stroke="#1e1e21" stroke-width=".35"/><path d="M.3 3.6 Q1.5 2.2 2.7 3.6" fill="none" stroke="#1e1e21" stroke-width=".35"/><circle cx="6.5" cy="1.8" r="1.1" fill="none" stroke="#1e1e21" stroke-width=".35"/><path d="M7.3 2.6 L8.2 3.5" stroke="#1e1e21" stroke-width=".35"/><path d="M10.6 1 H11.3 L12 3 H13.4 L13.8 1.6 H11.5" fill="none" stroke="#1e1e21" stroke-width=".35"/><circle cx="13.7" cy=".8" r=".7" fill="#e8392f"/></svg>
    </header>
    <div class="inner-hero" role="img" aria-label="Bronze metallic stiletto heel on a dark floor" style="background:linear-gradient(90deg,#3b332d,#5e4d40 45%,#b88a66 68%,#3a3534 88%,#272626)">
      <h1>TarnWisp</h1>
      <p>Aenean sollicitudin lorem quis bibendum auctor amet nibh vulputate dummy...</p>
    </div>
    <h2 class="block-title" style="top:84px">About <b>Us</b></h2>
    <div class="red-rule" style="left:27px;top:95px"></div>
    <div class="photo" role="img" aria-label="Pair of tan woven leather sandals" style="left:27px;top:99px;width:43px;height:28px;border-radius:40%;background:radial-gradient(ellipse at 50% 55%,#d98a4a,#b8662e 55%,rgba(255,255,255,0) 72%)"></div>
    <div class="copy-col flow" style="top:83px">
      <p>Aenean sollicitudin, lorem quis bibendum auctor, nisi elit consequat ipsum, nec sagittis sem nibh id elit. Duis sed odio sit amet nibh vulputate cursus a sit amet mauris. Morbi accumsan ipsum velit.</p>
      <p>Nam nec tellus a odio tincidunt auctor a ornare odio. Sed non mauris vitae erat consequat auctor eu in elit. Class aptent taciti sociosqu litora torquent per conubia nostra, per inceptos himenaeos. Mauris in erat justo. Nullam ac urna eu felis dapibus condimentum sit amet a augue.</p>
      <p>Aenean sollicitudin, lorem quis bibendum auctor, nisi elit consequat ipsum, nec sagittis sem nibh id elit. Duis sed odio sit amet nibh vulputate cursus a sit amet mauris. Morbi accumsan ipsum velit.</p>
      <p>Nam nec tellus a odio tincidunt auctor a ornare odio. Sed non mauris vitae erat consequat auctor eu in elit. Class aptent taciti sociosqu litora torquent per conubia nostra, per inceptos himenaeos. Mauris in erat justo. Nullam ac urna eu felis dapibus condimentum sit amet a augue.</p>
    </div>
    <p style="left:79px;top:150px;font-family:var(--serif);font-weight:700;font-size:2.8px">Transparency is our middle name.</p>
    <p style="left:79px;top:154.5px;width:89px;text-align:right;font-family:var(--serif);font-weight:700;font-size:2.8px">Take a look at how we live up to it</p>
    <svg style="left:168px;top:153px" width="10" height="5" viewBox="0 0 10 5" aria-hidden="true"><path d="M0 3 Q4 0 8 3 M7 1.7 L8 3 L6.6 3.6" fill="none" stroke="#e8392f" stroke-width=".35"/></svg>
    <h3 class="side-title" style="top:167px">When you buy, we make <b>money.</b></h3>
    <p class="copy-col" style="top:165px">Nam nec tellus a odio tincidunt auctor a ornare odio. Sed non mauris vitae erat consequat auctor eu in elit. Class aptent taciti sociosqu litora torquent per conubia nostra, per inceptos himenaeos. Mauris in erat justo. Nullam ac urna eu felis dapibus condimentum sit amet a augue.</p>
    <h3 class="side-title" style="top:189px">Most products don't make the <b>cut.</b></h3>
    <p class="copy-col" style="top:188px">Nam nec tellus a odio tincidunt auctor a ornare odio. Sed non mauris vitae erat consequat auctor eu in elit. Class aptent taciti sociosqu litora torquent per conubia nostra, per inceptos himenaeos. Mauris in erat justo. Nullam ac urna eu felis dapibus condimentum sit amet a augue.</p>
    <h2 class="block-title" style="top:212px">Our <b>Team</b></h2>
    <div class="red-rule" style="left:27px;top:222px"></div>
    <div class="photo team-photo" role="img" aria-label="Portrait of the founder" style="left:79px;background:linear-gradient(160deg,#8e8e8e,#c9b6a4)"></div>
    <div class="photo team-photo" role="img" aria-label="Portrait of the editor" style="left:110px;background:linear-gradient(160deg,#d8c9bd,#b79a86)"></div>
    <div class="photo team-photo" role="img" aria-label="Portrait of the co-founder" style="left:141px;background:linear-gradient(160deg,#6b5548,#a58670)"></div>
    <p class="team-name" style="left:79px">Ravi Ostrand</p><p class="team-role" style="left:79px">Founder</p><p class="team-copy" style="left:79px">Nam nec tellus a odio tincidunt ornare odio. Sed non mauris vitae erat consequat auctor eu in elit.</p>
    <p class="team-name" style="left:110px">Mira Feldon</p><p class="team-role" style="left:110px">Editor</p><p class="team-copy" style="left:110px">Nam nec tellus a odio tincidunt ornare odio. Sed non mauris vitae erat consequat auctor eu in elit.</p>
    <p class="team-name" style="left:141px">Theo Brannick</p><p class="team-role" style="left:141px">Founder</p><p class="team-copy" style="left:141px">Nam nec tellus a odio tincidunt ornare odio. Sed non mauris vitae erat consequat auctor eu in elit.</p>
    <footer class="site-footer">
      <div class="foot-col c1"><h4>Let us help you</h4><ul><li>Search</li><li>About Us</li><li>Footwear Size</li><li>Care Guide</li><li>Shipping</li><li>Contact</li><li>FAQS</li></ul></div>
      <div class="foot-col c2"><h4>Information</h4><ul><li>Site Map</li><li>Terms &amp; Condition</li><li>Privacy Policy</li><li>FAQs</li><li>Customer Service</li><li>Disclaimer</li></ul></div>
      <div class="foot-col c3"><h4>Contact Us</h4><span class="contact-item">Email:<br>hello@tarnwisp.com</span><span class="contact-item">Phone:<br>(+00) 123 456 7890</span><span class="contact-item">Office Location:<br>Some address line goes here city name</span></div>
      <div class="foot-col c4"><h4>Stay Connected</h4><div class="dot-row"><span style="background:#3d5a98"></span><span style="background:#3fa6e0"></span><span style="background:#d2407e"></span></div><h4>Payment Method</h4><div class="pay-row"><span style="background:#dfe3ea"></span><span style="background:#2a3f9e"></span><span style="background:#2b2b2b"></span><span style="background:#eaeaea"></span></div></div>
      <div class="copy-rule"></div>
      <p class="copyright">© COPYRIGHT 2021 - ALL RIGHTS RESERVED</p>
      <span class="to-top"></span>
    </footer>
  </section>

  <!-- BLOG DETAIL -->
  <section class="page detail">
    <header class="site-nav">
      <div class="nav-links"><span>MEN ▾</span><span>WOMEN ▾</span><span>KIDS ▾</span><span>FAVORITES</span><span>CUSTOMIZE</span></div>
      <div class="nav-logo">TarnWisp</div>
      <div class="nav-utility"><span>ABOUT</span><span>CONTACT US</span></div>
      <svg class="nav-icons" width="14" height="4" viewBox="0 0 14 4" aria-hidden="true"><circle cx="1.5" cy="1.3" r=".8" fill="none" stroke="#1e1e21" stroke-width=".35"/><path d="M.3 3.6 Q1.5 2.2 2.7 3.6" fill="none" stroke="#1e1e21" stroke-width=".35"/><circle cx="6.5" cy="1.8" r="1.1" fill="none" stroke="#1e1e21" stroke-width=".35"/><path d="M7.3 2.6 L8.2 3.5" stroke="#1e1e21" stroke-width=".35"/><path d="M10.6 1 H11.3 L12 3 H13.4 L13.8 1.6 H11.5" fill="none" stroke="#1e1e21" stroke-width=".35"/><circle cx="13.7" cy=".8" r=".7" fill="#e8392f"/></svg>
    </header>
    <div class="photo" role="img" aria-label="Navy running shoes hanging by pink laces on a pink wall" style="left:15px;top:25px;width:111px;height:69px;background:radial-gradient(ellipse at 52% 60%,#3a4560 0,#5a6077 18%,#f2b5c2 40%,#f4bfcb 100%)"></div>
    <h2 style="left:15px;top:101px;font-family:var(--serif);font-weight:700;font-size:5.8px">Some Blog Heading Goes Here</h2>
    <div class="photo" role="img" aria-label="Author avatar" style="left:15px;top:110px;width:7px;height:7px;border-radius:50%;background:#b59a88"></div>
    <p style="left:24px;top:111px;font-size:1.5px">By Mira Feldon</p>
    <p style="left:24px;top:114px;font-size:1.4px;color:var(--muted)">MAY 20, 2021 / 1 MIN READ</p>
    <p style="left:15px;top:123px;font-size:1.4px;color:var(--muted);word-spacing:3px">April 20, 2021 &nbsp; 0 Comment &nbsp; By Lena Hask</p>
    <div class="share-btns"><span style="background:#3d5a98">SHARE</span><span style="background:#3fa6e0">POST</span><span style="background:#dd4b39">SAVE</span><span style="background:#1d6fa5">SEND</span></div>
    <svg style="left:96px;top:131.5px" width="3" height="3" viewBox="0 0 3 3" aria-hidden="true"><circle cx=".6" cy="1.5" r=".45" fill="#333"/><circle cx="2.4" cy=".6" r=".45" fill="#333"/><circle cx="2.4" cy="2.4" r=".45" fill="#333"/><path d="M.6 1.5 L2.4 .6 M.6 1.5 L2.4 2.4" stroke="#333" stroke-width=".2"/></svg>
    <div class="detail-copy flow" style="top:139px">
      <p>Proin gravida nibh vel velit auctor aliquet. Aenean sollicitudin, lorem quis bibendum auctor, nisi elit sequat ipsum, nec sagittis sem nibh id elit. Duis sed odio sit amet nibh vulputate cursus a sit amet mauris. Morbi accumsan ipsum velit. Nam nec tellus a odio tincidunt auctor a ornare odio. Sed non mauris vitae erat consequat auctor eu in elit. Class aptent taciti litora torquent per conubia nostra.</p>
      <h3>The Best Product TarnWisp</h3>
      <p>Lorem ipsum proin gravida nibh vel velit auctor aliquet aenean sollicitudin lorem quis bibendum auctor, nisi elit consequat ipsum, nec litis sem nibh id elit. Duis sed odio sit amet nibh vulputate cursus a sit amet mauris. Morbi accumsan ipsum velit. Nam nec tellus a odio auctor...</p>
      <h3>Best Footwear</h3>
      <p>Lorem ipsum proin gravida nibh vel velit auctor aliquet aenean sollicitudin lorem quis bibendum auctor, nisi elit consequat ipsum, nec litis sem nibh id elit. Duis sed odio sit amet...</p>
      <h3>The Bottom Line</h3>
      <p>Lorem ipsum proin gravida nibh vel velit auctor aliquet aenean sollicitudin lorem quis bibendum auctor, nisi elit consequat ipsum, nec litis sem nibh id elit. Duis sed odio sit amet nibh vulputate cursus a sit amet mauris. Morbi accumsan ipsum velit. Nam nec tellus a odio auctor...</p>
      <h3>The Best Product TarnWisp</h3>
      <p>Lorem ipsum proin gravida nibh vel velit auctor aliquet aenean sollicitudin.</p>
    </div>
    <div class="share-bar">SHARE THIS STORY, CHOOSE YOUR PLATFORM!</div>
    <div style="left:106px;top:238.5px;display:flex;gap:1.5px"><span style="position:static;width:3px;height:3px;border-radius:50%;background:#555"></span><span style="position:static;width:3px;height:3px;border-radius:50%;background:#555"></span><span style="position:static;width:3px;height:3px;border-radius:50%;background:#555"></span></div>
    <p style="left:15px;top:255px;font-size:2.3px;font-weight:600">01 COMMENT</p>
    <div style="left:15px;top:259.5px;width:111px;height:.3px;background:var(--line)"></div>
    <div class="photo" role="img" aria-label="Commenter avatar" style="left:15px;top:266px;width:9px;height:9px;border-radius:50%;background:#c4a090"></div>
    <p style="left:27px;top:267px;font-size:1.7px;font-weight:600">STEPWREN</p>
    <p style="left:27px;top:270px;font-size:1.6px;color:var(--muted)">Love your work! Inspirational.</p>
    <p style="left:27px;top:276px;font-size:1.3px;color:var(--muted)">2 years ago &nbsp; Like &nbsp; Reply</p>
    <div class="reply-box">
      <h3 style="left:11px;top:6px;font-family:var(--serif);font-size:4.8px;font-weight:400">Leave a Replay</h3>
      <span class="field" style="left:11px;top:15px;width:43px">Enter your name</span>
      <span class="field" style="left:56px;top:15px;width:43px">Enter your email</span>
      <span class="field" style="left:11px;top:23.5px;width:43px">Enter your phone number</span>
      <span class="field" style="left:56px;top:23.5px;width:43px">Enter your address</span>
      <span class="field" style="left:11px;top:32px;width:88px;height:27px;line-height:5px">Type your message</span>
      <p style="left:11px;top:66px;font-size:1.5px">Required fields are marked*</p>
      <span style="left:75px;top:64px;width:24px;height:6.5px;background:var(--red);color:var(--paper);font-size:1.6px;font-weight:600;text-align:center;line-height:6.5px">POST COMMENT</span>
    </div>
    <h2 class="topics-title" style="top:26px">Related <b>Topics</b></h2>
    <ul class="topic-list" style="top:41px"><li>FLIP-FLOPS<span>→</span></li><li>SANDALS<span>→</span></li><li>SHOES<span>→</span></li><li>FLATS<span>→</span></li><li>HEELS<span>→</span></li><li>ETHNIC<span>→</span></li><li>SLIPPERS<span>→</span></li><li>CASUALS<span>→</span></li><li>FORMALS<span>→</span></li></ul>
    <footer class="site-footer" style="height:66px">
      <div class="foot-col c1"><h4>Let us help you</h4><ul><li>Search</li><li>About Us</li><li>Footwear Size</li><li>Care Guide</li><li>Shipping</li><li>Contact</li><li>FAQS</li></ul></div>
      <div class="foot-col c2"><h4>Information</h4><ul><li>Site Map</li><li>Terms &amp; Condition</li><li>Privacy Policy</li><li>FAQs</li><li>Customer Service</li><li>Disclaimer</li></ul></div>
      <div class="foot-col c3"><h4>Contact Us</h4><span class="contact-item">Email:<br>hello@tarnwisp.com</span><span class="contact-item">Phone:<br>(+00) 123 456 7890</span><span class="contact-item">Office Location:<br>Some address line goes here city name</span></div>
      <div class="foot-col c4"><h4>Stay Connected</h4><div class="dot-row"><span style="background:#3d5a98"></span><span style="background:#3fa6e0"></span><span style="background:#d2407e"></span></div><h4>Payment Method</h4><div class="pay-row"><span style="background:#dfe3ea"></span><span style="background:#2a3f9e"></span><span style="background:#2b2b2b"></span><span style="background:#eaeaea"></span></div></div>
      <div class="copy-rule"></div>
      <p class="copyright">© COPYRIGHT 2021 - ALL RIGHTS RESERVED</p>
      <span class="to-top"></span>
    </footer>
  </section>

  <!-- BLOG ARCHIVE -->
  <section class="page archive">
    <header class="site-nav">
      <div class="nav-links"><span>MEN ▾</span><span>WOMEN ▾</span><span>KIDS ▾</span><span>FAVORITES</span><span>CUSTOMIZE</span></div>
      <div class="nav-logo">TarnWisp</div>
      <div class="nav-utility"><span>ABOUT</span><span>CONTACT US</span></div>
      <svg class="nav-icons" width="14" height="4" viewBox="0 0 14 4" aria-hidden="true"><circle cx="1.5" cy="1.3" r=".8" fill="none" stroke="#1e1e21" stroke-width=".35"/><path d="M.3 3.6 Q1.5 2.2 2.7 3.6" fill="none" stroke="#1e1e21" stroke-width=".35"/><circle cx="6.5" cy="1.8" r="1.1" fill="none" stroke="#1e1e21" stroke-width=".35"/><path d="M7.3 2.6 L8.2 3.5" stroke="#1e1e21" stroke-width=".35"/><path d="M10.6 1 H11.3 L12 3 H13.4 L13.8 1.6 H11.5" fill="none" stroke="#1e1e21" stroke-width=".35"/><circle cx="13.7" cy=".8" r=".7" fill="#e8392f"/></svg>
    </header>
    <div class="inner-hero" role="img" aria-label="Crossed legs in black sneakers with coral laces" style="background:linear-gradient(90deg,#4d4c4b,#5c5a58 45%,#2f2e30 62%,#e58a7a 74%,#3c3b3c 86%,#555)">
      <h1 style="font-weight:400">Archives</h1>
      <p>Aenean sollicitudin lorem quis bibendum auctor amet nibh vulputate dummy...</p>
    </div>
    <h2 class="topics-title" style="left:14px;top:83px">Our Latest <b>Articles</b></h2>
    <div style="left:14px;top:91.5px;width:115px;height:.3px;background:var(--line)"></div>
    <div class="red-rule" style="left:14px;top:91.3px"></div>
    <article class="post-row" style="top:98px"><div class="photo" role="img" aria-label="Navy running shoes on pink" style="background:linear-gradient(135deg,#f2b5c2,#5a6077 60%,#f4bfcb)"></div><p class="row-meta">By John • January 2021</p><h3 class="row-title">Some Blog Heading Goes Here</h3><p class="row-copy">Duis sed odio sit amet nibh vulputate cursus a sit amet mauris morbi accumsan ipsum velit nam tellus a odio tincidunt auctor a ornare odio.</p><span class="row-read">READ →</span></article>
    <article class="post-row" style="top:134px"><div class="photo" role="img" aria-label="Black pumps on a beige floor" style="background:linear-gradient(135deg,#f0c8a6,#d79e78)"></div><p class="row-meta">By John • January 2021</p><h3 class="row-title">Some Blog Heading Goes Here</h3><p class="row-copy">Duis sed odio sit amet nibh vulputate cursus a sit amet mauris morbi accumsan ipsum velit nam tellus a odio tincidunt auctor a ornare odio.</p><span class="row-read">READ →</span></article>
    <article class="post-row" style="top:170px"><div class="photo" role="img" aria-label="Cream slip-on shoes on light wood" style="background:linear-gradient(135deg,#c9bfae,#ece6da)"></div><p class="row-meta">By John • January 2021</p><h3 class="row-title">Some Blog Heading Goes Here</h3><p class="row-copy">Duis sed odio sit amet nibh vulputate cursus a sit amet mauris morbi accumsan ipsum velit nam tellus a odio tincidunt auctor a ornare odio.</p><span class="row-read">READ →</span></article>
    <article class="post-row" style="top:206px"><div class="photo" role="img" aria-label="Brown baby shoes on white" style="background:linear-gradient(135deg,#eeeeee,#a9714a 55%,#efefef)"></div><p class="row-meta">By John • January 2021</p><h3 class="row-title">Some Blog Heading Goes Here</h3><p class="row-copy">Duis sed odio sit amet nibh vulputate cursus a sit amet mauris morbi accumsan ipsum velit nam tellus a odio tincidunt auctor a ornare odio.</p><span class="row-read">READ →</span></article>
    <article class="post-row" style="top:242px"><div class="photo" role="img" aria-label="White slides on pink and yellow" style="background:linear-gradient(135deg,#f6c5cf,#f3f0c0 55%,#ecef9a)"></div><p class="row-meta">By John • January 2021</p><h3 class="row-title">Some Blog Heading Goes Here</h3><p class="row-copy">Duis sed odio sit amet nibh vulputate cursus a sit amet mauris morbi accumsan ipsum velit nam tellus a odio tincidunt auctor a ornare odio.</p><span class="row-read">READ →</span></article>
    <nav class="pager"><span style="background:var(--mist)">‹</span><span>1</span><span>2</span><span style="background:var(--red);color:var(--paper)">3</span><span>4</span><span>9</span><span style="background:var(--mist)">›</span></nav>
    <h2 class="topics-title" style="top:83px">Related <b>Topics</b></h2>
    <ul class="topic-list" style="top:94px"><li>FLIP-FLOPS<span>→</span></li><li>SANDALS<span>→</span></li><li>SHOES<span>→</span></li><li>FLATS<span>→</span></li><li>HEELS<span>→</span></li><li>ETHNIC<span>→</span></li><li>SLIPPERS<span>→</span></li><li>CASUALS<span>→</span></li><li>FORMALS<span>→</span></li></ul>
    <footer class="site-footer">
      <div class="foot-col c1"><h4>Let us help you</h4><ul><li>Search</li><li>About Us</li><li>Footwear Size</li><li>Care Guide</li><li>Shipping</li><li>Contact</li><li>FAQS</li></ul></div>
      <div class="foot-col c2"><h4>Information</h4><ul><li>Site Map</li><li>Terms &amp; Condition</li><li>Privacy Policy</li><li>FAQs</li><li>Customer Service</li><li>Disclaimer</li></ul></div>
      <div class="foot-col c3"><h4>Contact Us</h4><span class="contact-item">Email:<br>hello@tarnwisp.com</span><span class="contact-item">Phone:<br>(+00) 123 456 7890</span><span class="contact-item">Office Location:<br>Some address line goes here city name</span></div>
      <div class="foot-col c4"><h4>Stay Connected</h4><div class="dot-row"><span style="background:#3d5a98"></span><span style="background:#3fa6e0"></span><span style="background:#d2407e"></span></div><h4>Payment Method</h4><div class="pay-row"><span style="background:#dfe3ea"></span><span style="background:#2a3f9e"></span><span style="background:#2b2b2b"></span><span style="background:#eaeaea"></span></div></div>
      <div class="copy-rule"></div>
      <p class="copyright">© COPYRIGHT 2021 - ALL RIGHTS RESERVED</p>
      <span class="to-top"></span>
    </footer>
  </section>
</main>
</body>
</html>
```